2017 Summer Camp Marketing Poster

We need a poster 11 X 17 to advertise our summer 2017 programs for Camp Tellumar and direct interested people to our website tellumar.org.

The poster will grab peoples eye especially kids and make them want to further explore our camp.

There will be a call to action "Sign up today for the summer of a lifetime"

The poster will primarily be hung in churches where most people know about the camp but need reminded of our summer camp programs and dates.

Target Market(s)

Kids and Families

Industry/Entity Type

Marketing

Font styles to use
Sans Serif

```html
<!DOCTYPE html>
<html lang="en">
<head>
<meta charset="utf-8">
<title>Summer 2017 at Camp Tellumar – Poster</title>
<link rel="stylesheet" href="https://fonts.googleapis.com/css2?family=Righteous&family=Montserrat:wght@500;600;700&display=swap">
<style>
  :root {
    --page: #ffffff;
    --orange: #ee6c24;
    --sky: #8fd6ec;
    --sky-mid: #6cc0d8;
    --teal: #74c6b6;
    --foliage: #5fa7a8;
    --white: #ffffff;
  }
  html, body {
    margin: 0;
    width: 1200px;
    height: 1200px;
    overflow: hidden;
    background: var(--page);
  }
  .canvas {
    position: relative;
    width: 1200px;
    height: 1200px;
  }
  .poster {
    position: absolute;
    left: 255px;
    top: 106px;
    width: 621px;
    height: 960px;
    display: block;
  }
  .title {
    font-family: "Righteous", sans-serif;
    fill: var(--orange);
    text-anchor: middle;
  }
  .details {
    font-family: "Montserrat", sans-serif;
    font-weight: 500;
    font-size: 18px;
    fill: var(--white);
    text-anchor: middle;
    letter-spacing: 0.5px;
  }
  .dates {
    font-family: "Montserrat", sans-serif;
    font-weight: 700;
    font-size: 16px;
    fill: var(--white);
    text-anchor: middle;
    letter-spacing: 0.5px;
  }
  .cta {
    font-family: "Montserrat", sans-serif;
    font-weight: 700;
    font-size: 30px;
    fill: var(--white);
    text-anchor: middle;
    letter-spacing: 1px;
  }
  .cta-accent { fill: var(--orange); }
  .url {
    font-family: "Montserrat", sans-serif;
    font-weight: 700;
    font-size: 46px;
    fill: var(--orange);
    text-anchor: end;
  }
  .photo-ring { fill: none; stroke: var(--orange); stroke-width: 4; }
  .dotted-ring { fill: none; stroke: var(--white); stroke-width: 2.5; stroke-dasharray: 0.1 6; stroke-linecap: round; }
</style>
</head>
<body>
<div class="canvas">
  <svg class="poster" viewBox="0 0 621 960" xmlns="http://www.w3.org/2000/svg">
    <defs>
      <linearGradient id="bg-grad" x1="0" y1="0" x2="0" y2="1">
        <stop offset="0" stop-color="#94d9ee"/>
        <stop offset="0.45" stop-color="#6fbfd6"/>
        <stop offset="1" stop-color="#79cab5"/>
      </linearGradient>
      <radialGradient id="tree-haze" cx="0.55" cy="0.45" r="0.55">
        <stop offset="0" stop-color="#5fa7a8" stop-opacity="0.55"/>
        <stop offset="1" stop-color="#5fa7a8" stop-opacity="0"/>
      </radialGradient>
      <linearGradient id="photo-group" x1="0" y1="0" x2="0" y2="1">
        <stop offset="0" stop-color="#6f9a4e"/>
        <stop offset="1" stop-color="#5bb8a5"/>
      </linearGradient>
      <linearGradient id="photo-jump" x1="0" y1="0" x2="0" y2="1">
        <stop offset="0" stop-color="#b9dcef"/>
        <stop offset="1" stop-color="#6d7f8a"/>
      </linearGradient>
      <linearGradient id="photo-helmets" x1="0" y1="0" x2="0" y2="1">
        <stop offset="0" stop-color="#5b8a3a"/>
        <stop offset="1" stop-color="#b5443a"/>
      </linearGradient>
      <linearGradient id="photo-climb" x1="0" y1="0" x2="0" y2="1">
        <stop offset="0" stop-color="#c4a57d"/>
        <stop offset="1" stop-color="#a88862"/>
      </linearGradient>
    </defs>

    <!-- background -->
    <rect class="backdrop" width="621" height="960" fill="url(#bg-grad)"/>
    <rect class="backdrop-photo" width="621" height="960" fill="url(#tree-haze)" role="img" aria-label="Soft-focus photo of a leafy tree against a blue summer sky"/>

    <!-- bands -->
    <rect class="band band-top" x="0" y="0" width="621" height="31" fill="var(--orange)"/>
    <rect class="band band-bottom" x="0" y="927" width="621" height="33" fill="var(--orange)"/>

    <!-- headline -->
    <text class="title title-main" x="310" y="152" font-size="76" textLength="518" lengthAdjust="spacingAndGlyphs">SUMMER 2017</text>
    <text class="title title-sub" x="310" y="207" font-size="46" textLength="466" lengthAdjust="spacingAndGlyphs">AT CAMP TELLUMAR</text>
    <text class="details" x="310" y="236">Established 1952</text>
    <text class="details" x="310" y="259">Cedar Falls, IN</text>
    <text class="dates" x="310" y="281">June 11 – August 4, 2017</text>

    <!-- photo cluster -->
    <g class="photo-cluster">
      <circle class="dotted-ring" cx="161" cy="516" r="152"/>
      <circle class="dotted-ring" cx="349" cy="398" r="103"/>
      <circle class="dotted-ring" cx="501" cy="458" r="95"/>
      <circle class="dotted-ring" cx="377" cy="586" r="122"/>

      <circle class="photo" cx="161" cy="516" r="136" fill="url(#photo-group)" role="img" aria-label="Photo of smiling teen campers pointing toward the viewer"/>
      <circle class="photo-ring" cx="161" cy="516" r="136"/>

      <circle class="photo" cx="349" cy="398" r="92" fill="url(#photo-jump)" role="img" aria-label="Photo of campers jumping off a dock into a lake"/>
      <circle class="photo-ring" cx="349" cy="398" r="92"/>

      <circle class="photo" cx="501" cy="458" r="84" fill="url(#photo-helmets)" role="img" aria-label="Photo of young campers in helmets and harnesses giving a thumbs up"/>
      <circle class="photo-ring" cx="501" cy="458" r="84"/>

      <circle class="photo" cx="377" cy="586" r="110" fill="url(#photo-climb)" role="img" aria-label="Photo of kids climbing a wooden climbing wall"/>
      <circle class="photo-ring" cx="377" cy="586" r="110"/>
    </g>

    <!-- call to action -->
    <text class="cta" x="310" y="775"><tspan class="cta-accent">SIGN UP TODAY</tspan> FOR THE</text>
    <text class="cta" x="310" y="809">SUMMER OF A LIFETIME</text>

    <text class="url" x="440" y="884">tellumar.org</text>

    <!-- click cursor icon -->
    <g class="cursor-icon" fill="var(--white)" stroke="var(--white)" stroke-linecap="round">
      <path d="M464 870 L464 906 L473 897 L480 911 L486 908 L479 894 L491 894 Z" stroke="none"/>
      <line x1="456" y1="872" x2="449" y2="870" stroke-width="2.5"/>
      <line x1="458" y1="864" x2="452" y2="858" stroke-width="2.5"/>
      <line x1="466" y1="861" x2="466" y2="853" stroke-width="2.5"/>
      <line x1="456" y1="880" x2="450" y2="885" stroke-width="2.5"/>
    </g>
  </svg>
</div>
</body>
</html>
```